Quorvin Upcoming Gigs

One page graphic with my upcoming dates. Logo and photo attached, and sample from last flyer. Text:

QUORVIN

UPCOMING DATES

3/26/18 Tidal Plums (Las Vegas, NV)

4/1/18 Venture Hollow 2847 M St (Sac, CA)

4/8/18 Amber Heron (Sac, CA)

5/5/18 Low Ceiling @ Silver Moth (Sac, CA)

5/10/18 Pellman Art Museum (Sac, CA)

5/11/18 Vif Brume @ Cafe du Lierre (Sac, CA)

5/27/18 Sonnlicht JTR @ Vox (Sac, CA)

Save The Date: 9/21/18 Lanterns Festival (Puerto Nuevo, MX)

plazabook.example/quorvin482

Target Market(s)

House/Electronic Music

Industry/Entity Type

Night Club

Font styles to use
Sans Serif

Colors

Designer to choose colors to be used in the design.

Requirements
Must have
• Quorvin logo or something that looks good instead. Prefer photo to be in but not necessary.
Nice to have

```html
<!DOCTYPE html>
<html lang="en">
<head>
<meta charset="utf-8">
<title>Quorvin Upcoming Dates</title>
<link rel="stylesheet" href="https://fonts.googleapis.com/css2?family=Exo+2:wght@500&family=Montserrat:wght@400;600;700;800;900&display=swap">
<style>
  :root {
    --page: #1c1a1f;
    --night: #0b0b3a;
    --indigo: #1a1670;
    --violet: #3b1f9a;
    --magenta: #c2207a;
    --pink: #ff5aa8;
    --ink: #000000;
    --white: #ffffff;
    --gold: #f7c90a;
    --cyan: #1fb8f0;
    --neon: #5fd0ff;
    --frame: #1aa8e0;
  }
  * { box-sizing: border-box; margin: 0; padding: 0; }
  html, body {
    width: 1200px; height: 1200px; overflow: hidden;
    background: var(--page);
    font-family: "Montserrat", Arial, sans-serif;
  }
  .flyer {
    position: absolute; left: 40px; top: 307px;
    width: 1120px; height: 585px;
    border: 1px solid var(--frame);
    overflow: hidden;
    background:
      radial-gradient(ellipse at 70% 35%, var(--violet) 0%, transparent 55%),
      linear-gradient(180deg, var(--indigo) 0%, var(--night) 70%, #050518 100%);
  }
  .artist-photo {
    position: absolute; right: 0; top: 0;
    width: 660px; height: 100%;
    background:
      radial-gradient(ellipse at 58% 50%, var(--pink) 0%, var(--magenta) 28%, rgba(90,30,150,0.6) 55%, transparent 75%),
      linear-gradient(180deg, transparent 70%, var(--ink) 100%);
  }
  .brand {
    position: absolute; left: 44px; top: 30px;
    font-weight: 900; font-size: 80px; line-height: 1;
    letter-spacing: 1px; color: var(--white);
  }
  .section-title {
    position: absolute; left: 44px; top: 140px;
    font-family: "Exo 2", Arial, sans-serif; font-weight: 500;
    font-size: 46px; line-height: 1; color: #e6f7ff;
    text-shadow: 0 0 4px var(--neon), 0 0 10px var(--cyan), 0 0 18px var(--cyan);
  }
  .gig-list { position: absolute; left: 40px; top: 198px; list-style: none; }
  .gig {
    display: flex; gap: 6px; height: 30px; padding: 3px 4px;
    margin-bottom: 8.8px; width: 420px;
    background: rgba(5,5,40,0.55);
  }
  .gig-date, .gig-venue {
    border: 1.5px solid var(--gold); height: 24px;
    font-size: 16px; line-height: 21px;
  }
  .gig-date {
    width: 76px; background: var(--gold); color: var(--ink);
    text-align: right; padding-right: 5px; font-weight: 500;
  }
  .gig-venue { flex: 1; color: var(--white); padding-left: 8px; letter-spacing: 0.3px; }
  .gig-place { color: var(--cyan); font-weight: 700; }
  .save-date { position: absolute; left: 46px; top: 482px; }
  .save-label { color: var(--gold); font-weight: 700; font-size: 14px; letter-spacing: 0.5px; }
  .save-day { color: var(--cyan); font-weight: 700; font-size: 29px; line-height: 1.15; }
  .save-event { color: var(--white); font-size: 16px; }
  .save-event strong { font-weight: 700; }
  .follow {
    position: absolute; right: 0; bottom: 0;
    width: 322px; height: 88px; background: var(--ink);
    color: var(--white); text-align: right; padding: 35px 36px 0 0;
  }
  .follow-title { font-weight: 700; font-size: 12px; letter-spacing: 0.6px; }
  .follow-link { font-size: 9.5px; margin-top: 3px; display: flex; justify-content: flex-end; align-items: center; gap: 4px; }
  .follow-link i { width: 8px; height: 8px; background: var(--cyan); display: inline-block; }
</style>
</head>
<body>
  <section class="flyer">
    <div class="artist-photo" role="img" aria-label="Photo of the DJ at the decks under pink and purple lights against a brick wall"></div>
    <div class="brand">QUORVIN</div>
    <h1 class="section-title">UPCOMING DATES</h1>
    <ul class="gig-list">
      <li class="gig"><span class="gig-date">3/26/18</span><span class="gig-venue">Tidal Plums <span class="gig-place">(Las Vegas, NV)</span></span></li>
      <li class="gig"><span class="gig-date">4/01/18</span><span class="gig-venue">Venture Hollow 2847 M St <span class="gig-place">(Sac, CA)</span></span></li>
      <li class="gig"><span class="gig-date">4/08/18</span><span class="gig-venue">Amber Heron <span class="gig-place">(Sac, CA)</span></span></li>
      <li class="gig"><span class="gig-date">5/05/18</span><span class="gig-venue">Low Ceiling @ Silver Moth <span class="gig-place">(Sac, CA)</span></span></li>
      <li class="gig"><span class="gig-date">5/10/18</span><span class="gig-venue">Pellman Art Museum <span class="gig-place">(Sac, CA)</span></span></li>
      <li class="gig"><span class="gig-date">5/11/18</span><span class="gig-venue">Vif Brume @ Cafe du Lierre <span class="gig-place">(Sac, CA)</span></span></li>
      <li class="gig"><span class="gig-date">5/27/18</span><span class="gig-venue">Sonnlicht JTR @ Vox <span class="gig-place">(Sac, CA)</span></span></li>
    </ul>
    <div class="save-date">
      <div class="save-label">SAVE THE DATE:</div>
      <div class="save-day">9/21/18</div>
      <div class="save-event"><strong>Lanterns Festival</strong> (Puerto Nuevo, MX)</div>
    </div>
    <div class="follow">
      <div class="follow-title">FOLLOW US ON</div>
      <div class="follow-link"><i></i>plazabook.example/quorvin482</div>
    </div>
  </section>
</body>
</html>
```